Building and Facilities Management brochure

Please refer to attached PDF, page by page with information about the brief.
SOPHISTICATED, BOLD, PROFESSIONAL BROCHURE to market our company in business meetings to Builders, Owners of buildings, Strata Committees etc.

The final design should portray quality, service, integrity,
Clear Communication

Attached is:
- pdf with details of basic layout options and wording and most of the information about the brief.
- Logo options to use
- Business card designs to understand what design we have previously had.
- Word document of the pdf if that helps to copy the information.

Target Market(s)

Professionals. Builders/developer, Strata Owners, and Building owners who want a high level of service and management of their building

Industry/Entity Type

It Company

Requirements
Must have
• - Logo
• - Contact details
• - Use of the colour in the design which has been specified.
• - Images/s of building/s
• - Use the phrase "Quality Service with Integrity"
Nice to have
• - as much of the wording as possible from the document which was uploaded, that will fit and work with the design
Should not have
• Excessive colour or variances as it needs to stay clear, bold and sophisticated.
• Too much on the page, clarity is key for clear communication without trying to clutter too much on the page.

```html
<!DOCTYPE html>
<html lang="en">
<head>
<meta charset="utf-8">
<title>Harlow Building Services – Brochure Cover</title>
<link rel="stylesheet" href="https://fonts.googleapis.com/css2?family=Open+Sans:wght@400;600&family=Lato:wght@300&display=swap">
<style>
  :root {
    --bg: #e6e6e6;
    --panel-back: #434b57;
    --panel-front: #414955;
    --brand-blue: #29abe2;
    --text-light: #f2f4f6;
    --tagline: #5f6876;
    --swoosh-white: #eef1f4;
  }
  * { box-sizing: border-box; margin: 0; padding: 0; }
  html, body {
    width: 1200px; height: 817px; overflow: hidden;
    background: var(--bg);
    font-family: "Open Sans", sans-serif;
  }
  .spread {
    position: absolute; left: 72px; top: 28px;
    width: 1056px; height: 760px;
    display: flex;
  }
  .panel { position: relative; width: 528px; height: 760px; overflow: hidden; }
  .panel--back { background: var(--panel-back); }
  .panel--front { background: var(--panel-front); }

  .brand-name {
    position: absolute; left: 0; right: 0; text-align: center;
    color: var(--brand-blue); font-weight: 600;
    text-transform: uppercase; letter-spacing: 0.08em;
  }
  .panel--back .brand-name { top: 186px; font-size: 17px; }
  .panel--front .brand-name { top: 84px; font-size: 20px; line-height: 1.35; }

  .contact-item {
    position: absolute; left: 0; right: 0; text-align: center;
    color: var(--text-light); font-size: 13.5px; line-height: 18px;
  }
  .contact-item svg { display: block; margin: 0 auto 10px; }
  .contact-item--area { top: 241px; }
  .contact-item--email { top: 362px; }
  .contact-item--web { top: 466px; }

  .cover-art { position: absolute; left: 0; top: 0; }

  .tagline {
    position: absolute; font-family: "Lato", sans-serif; font-weight: 300;
    color: var(--tagline); font-size: 56px; line-height: 1; letter-spacing: 0.02em;
    white-space: nowrap;
  }
  .tagline--quality { left: 56px; top: 560px; }
  .tagline--service { left: 134px; top: 617px; }
  .tagline--integrity { left: 193px; top: 673px; }
</style>
</head>
<body>
<main class="spread">
  <section class="panel panel--back" aria-label="Back cover">
    <div class="brand-name">Harlow Building Services</div>

    <div class="contact-item contact-item--area">
      <svg width="42" height="42" viewBox="0 0 42 42" aria-hidden="true">
        <circle cx="21" cy="21" r="19" fill="none" stroke="var(--brand-blue)" stroke-width="2"/>
        <path d="M21 31c-5-6-8-10-8-14a8 8 0 0 1 16 0c0 4-3 8-8 14z" fill="var(--brand-blue)"/>
        <circle cx="21" cy="17" r="3" fill="var(--panel-back)"/>
      </svg>
      Riverton and surrounding suburbs<br>through to the Eastvale Peninsula
    </div>

    <div class="contact-item contact-item--email">
      <svg width="42" height="42" viewBox="0 0 42 42" aria-hidden="true">
        <circle cx="21" cy="21" r="19" fill="none" stroke="var(--brand-blue)" stroke-width="2"/>
        <circle cx="21" cy="21" r="14" fill="var(--brand-blue)"/>
        <rect x="13" y="16" width="16" height="11" fill="var(--panel-back)" rx="1"/>
        <path d="M13 16l8 6 8-6M13 27l6-5M29 27l-6-5" fill="none" stroke="var(--brand-blue)" stroke-width="1.3"/>
      </svg>
      info@harlowbuildingservices.com.au
    </div>

    <div class="contact-item contact-item--web">
      <svg width="42" height="42" viewBox="0 0 42 42" aria-hidden="true">
        <circle cx="21" cy="21" r="19" fill="none" stroke="var(--brand-blue)" stroke-width="2"/>
        <circle cx="21" cy="21" r="14" fill="var(--brand-blue)"/>
        <g fill="none" stroke="var(--panel-back)" stroke-width="1.3">
          <circle cx="21" cy="21" r="9"/>
          <ellipse cx="21" cy="21" rx="4" ry="9"/>
          <path d="M12 21h18M14 16h14M14 26h14"/>
        </g>
      </svg>
      www.harlowbuildingservices.com.au
    </div>
  </section>

  <section class="panel panel--front" aria-label="Front cover">
    <div class="brand-name">Harlow Building<br>Services</div>

    <svg class="cover-art" width="528" height="760" viewBox="0 0 528 760">
      <defs>
        <linearGradient id="cityTones" x1="0" y1="0" x2="0" y2="1">
          <stop offset="0" stop-color="#d9e2ea"/>
          <stop offset="0.3" stop-color="#9fb6cb"/>
          <stop offset="0.7" stop-color="#4f7596"/>
          <stop offset="1" stop-color="#2c4d6e"/>
        </linearGradient>
      </defs>
      <path class="band band--top" d="M0 222 Q250 150 528 196 L528 212 Q260 168 0 234 Z" fill="var(--brand-blue)"/>
      <path class="cover-photo" role="img" aria-label="Aerial photograph of a city skyline with high-rise office towers"
            d="M0 234 Q260 168 528 212 L528 500 Q330 505 200 468 Q80 438 0 418 Z" fill="url(#cityTones)"/>
      <path class="band band--swoosh" d="M0 418 Q80 438 200 468 Q330 505 528 500 L528 512 Q320 522 180 486 Q70 455 0 428 Z" fill="var(--swoosh-white)"/>
      <path class="band band--bottom" d="M190 502 Q360 538 528 518 L528 532 Q360 552 190 502 Z" fill="var(--brand-blue)"/>
    </svg>

    <div class="tagline tagline--quality">QUALITY</div>
    <div class="tagline tagline--service">SERVICE</div>
    <div class="tagline tagline--integrity">INTEGRITY</div>
  </section>
</main>
</body>
</html>
```